Art and Artifact Selling classy website.

I am into selling of Art works and artifacts. The art work range from different type such as animation, architecture, assemblage, calligraphy, computer, Christian or religious, conceptual, artistic design, drawing, folk, graffiti, graphic, illuminated manuscript, illustration, mosaic, painting, performance, photography, sculpture. This website will feature categories of the above art works. My website should have images of the above art works and should be classy. My business is based in the United States and my target customers are Americans. Different artistic colors are welcome. My business name is quenmarsh Art.

Industry/Entity Type

Architecture

Coding

Coded - Design and coding required

```html
<!DOCTYPE html>
<html lang="en">
<head>
<meta charset="utf-8">
<title>Quenmarsh Art — Art Gallery</title>
<link rel="stylesheet" href="https://fonts.googleapis.com/css2?family=Open+Sans:wght@400;600;700;800&display=swap">
<style>
:root{
  --orange:#f7780f;
  --orange-dark:#e56a05;
  --ink:#333333;
  --text:#555555;
  --muted:#777777;
  --dark:#2f2f2f;
  --footer:#2b2b2b;
  --light:#efefef;
  --field:#eeeeee;
  --white:#ffffff;
  --frame:#2a2a2a;
  --star:#ffd54a;
}
*{box-sizing:border-box;margin:0;padding:0}
html,body{width:1200px;height:3462px;overflow:hidden}
body{font-family:"Open Sans",Arial,sans-serif;color:var(--text);background:var(--white);position:relative}
.wrap{width:1050px;margin:0 auto;position:relative}
.btn{display:inline-block;background:var(--orange);color:var(--white);font-weight:700;font-size:14px;letter-spacing:.5px;text-transform:uppercase;text-align:center;line-height:46px;height:46px;width:152px}
.section-title{font-size:23px;font-weight:700;color:var(--ink);text-align:center;letter-spacing:.5px;text-transform:uppercase}
.section-lead{font-size:14px;color:var(--muted);text-align:center}

/* hero */
.hero{position:relative;height:623px;background:linear-gradient(100deg,#5b4634 0%,#7a5f49 35%,#8a7261 60%,#4a3a2e 100%);overflow:hidden}
.hero-shade{position:absolute;inset:0;background:linear-gradient(90deg,rgba(0,0,0,.35),rgba(0,0,0,.05))}
.topbar{position:absolute;top:40px;left:76px;right:76px;display:flex;align-items:center;white-space:nowrap}
.brand{color:var(--white);font-size:26px;font-weight:700;letter-spacing:.3px;text-transform:uppercase;margin-right:44px}
.nav{display:flex;list-style:none}
.nav li{color:var(--white);font-size:11px;font-weight:700;text-transform:uppercase;margin-right:27px;white-space:nowrap}
.nav-icons{margin-left:auto;display:flex;gap:22px}
.hero-copy{position:absolute;left:76px;top:222px;color:var(--white);z-index:2}
.hero-copy h1{font-size:35px;font-weight:800;line-height:45px;text-transform:uppercase;letter-spacing:.5px;white-space:nowrap}
.hero-copy p{font-size:19px;font-weight:700;margin-top:10px}
.hero-copy .btn{margin-top:22px}
.dots{position:absolute;left:76px;top:540px;display:flex;gap:8px}
.dots span{width:12px;height:12px;border-radius:50%;background:var(--ink)}
.dots span:first-child{background:var(--white)}
.collage-card{position:absolute;border:10px solid var(--white);box-shadow:0 6px 14px rgba(0,0,0,.4)}
.c1{left:578px;top:128px;width:320px;height:260px;transform:rotate(3deg);background:linear-gradient(135deg,#d83b2a,#f2c230 40%,#2d8f6f 70%,#2a3c7a)}
.c2{left:590px;top:370px;width:350px;height:210px;transform:rotate(6deg);background:linear-gradient(135deg,#d9cdb4,#a7bfd0 50%,#c9b690)}
.c3{left:808px;top:185px;width:345px;height:250px;transform:rotate(-4deg);background:linear-gradient(135deg,#efe2c4,#d3b894 50%,#9a7d5c)}

/* welcome */
.welcome{height:335px;text-align:center;padding-top:52px}
.welcome p{width:1040px;margin:22px auto 0;font-size:14px;line-height:23px;color:var(--text)}
.welcome .btn{margin-top:30px}

/* range */
.range{height:824px;background:var(--light);padding-top:64px}
.range .section-lead{margin-top:16px}
.art-grid{display:grid;grid-template-columns:repeat(4,242px);column-gap:28px;row-gap:24px;margin-top:48px}
.art-frame{height:178px;border:7px solid var(--frame);background:var(--white);padding:8px;box-shadow:0 2px 4px rgba(0,0,0,.3)}
.art-fill{width:100%;height:100%}
.art-label{font-size:14px;font-weight:700;color:var(--ink);text-transform:uppercase;text-align:center;margin-top:12px;letter-spacing:.3px}
.range .btn{display:block;margin:48px auto 0;width:180px}

/* sale */
.sale{height:561px;padding-top:52px}
.sale-head{display:flex;align-items:center;justify-content:space-between}
.sale-head h2{font-size:23px;font-weight:700;color:var(--ink);text-transform:uppercase;letter-spacing:.5px}
.cards{display:grid;grid-template-columns:repeat(4,242px);column-gap:28px;margin-top:38px}
.card{position:relative;height:369px;border:1px solid #dddddd;text-align:center}
.card-img{height:212px}
.card h3{font-size:13px;font-weight:700;color:var(--ink);text-transform:uppercase;margin-top:26px}
.card p{font-size:13px;line-height:19px;color:var(--text);width:170px;margin:6px auto 0}
.price{font-size:22px;font-weight:700;color:var(--orange);margin-top:8px}
.cart{position:absolute;left:50%;bottom:-20px;margin-left:-20px;width:40px;height:40px;border-radius:50%;background:var(--orange);display:flex;align-items:center;justify-content:center}

/* news + reviews */
.split{display:flex;height:387px}
.news{width:600px;background:var(--dark);padding:30px 0 0 76px;color:var(--white)}
.reviews{width:600px;background:var(--orange);padding:30px 0 0 38px;color:var(--white)}
.split h2{font-size:23px;font-weight:700;text-transform:uppercase;letter-spacing:.5px}
.news-item{display:flex;margin-top:26px}
.news-item:first-of-type{margin-top:22px}
.news-thumb{width:150px;height:107px;flex:none}
.news-body{margin-left:28px;width:300px}
.news-date{font-size:12px;font-weight:700;color:var(--orange)}
.news-body h3{font-size:15px;font-weight:700;margin-top:4px}
.news-body p{font-size:13px;line-height:19px;color:#bdbdbd;margin-top:4px}
.review{margin-top:24px;width:490px}
.review:first-of-type{margin-top:22px}
.stars{display:flex;gap:3px}
.review h3{font-size:14px;font-weight:700;margin-top:4px}
.review p{font-size:13px;line-height:19px;color:#ffe3c9;margin-top:4px}
.review .by{font-size:13px;font-weight:700;color:var(--ink);margin-top:10px}

/* signup */
.signup{height:356px;text-align:center;padding-top:34px}
.signup .section-lead{margin-top:18px}
.field{width:514px;height:46px;margin:0 auto;background:var(--field);font-size:12px;color:var(--ink);line-height:46px}
.field.first{margin-top:28px}
.field+.field{margin-top:9px}
.signup .btn{margin-top:19px;width:180px}

/* footer */
.footer{height:318px;background:var(--footer);color:#cccccc;position:relative}
.fcol{position:absolute;top:44px}
.fcol h4{font-size:13px;font-weight:700;color:var(--white);text-transform:uppercase;line-height:18px;margin-bottom:8px}
.fcol ul{list-style:none}
.fcol li{font-size:13px;line-height:28.5px}
.fcol.cont{top:70px}
.contact .name{font-size:13px;font-weight:700;color:var(--orange);text-transform:uppercase;line-height:28.5px}
.contact .addr{font-size:13px;line-height:20px;margin-top:2px}
.contact .row{display:flex;align-items:center;gap:8px;font-size:13px;line-height:28.5px;margin-top:4px}
.bottom{height:58px;background:var(--orange);display:flex;align-items:center;padding:0 76px;color:var(--white);font-size:12px}
.socials{margin-left:auto;display:flex;gap:22px}
.socials span{width:16px;height:16px;border-radius:50%;background:var(--white)}
</style>
</head>
<body>

<header class="hero">
  <div class="hero-shade"></div>
  <div class="collage-card c1" role="img" aria-label="Colourful graffiti artwork"></div>
  <div class="collage-card c3" role="img" aria-label="Painting of a violinist"></div>
  <div class="collage-card c2" role="img" aria-label="Hand-painted pattern sketch"></div>
  <div class="topbar">
    <div class="brand">Quenmarsh Art</div>
    <ul class="nav">
      <li>Home</li><li>About Artist</li><li>Gallery</li><li>Sale</li><li>Blog</li><li>Reviews</li><li>News Event</li><li>Contact</li>
    </ul>
    <div class="nav-icons">
      <svg width="14" height="14" viewBox="0 0 14 14"><circle cx="7" cy="4" r="3" fill="#fff"/><path d="M1 14c0-4 3-6 6-6s6 2 6 6z" fill="#fff"/></svg>
      <svg width="14" height="14" viewBox="0 0 14 14"><path d="M0 1h3l2 8h7l2-6H4" fill="none" stroke="#fff" stroke-width="2"/><circle cx="6" cy="12" r="1.5" fill="#fff"/><circle cx="11" cy="12" r="1.5" fill="#fff"/></svg>
      <svg width="14" height="14" viewBox="0 0 14 14"><circle cx="6" cy="6" r="4.5" fill="none" stroke="#fff" stroke-width="2"/><path d="M9 9l4 4" stroke="#fff" stroke-width="2"/></svg>
    </div>
  </div>
  <div class="hero-copy">
    <h1>Welcome to Quenmarsh<br>Art Gallery</h1>
    <p>I am selling of Art Works &amp; Artifacts</p>
    <span class="btn">Read More</span>
  </div>
  <div class="dots"><span></span><span></span><span></span><span></span></div>
</header>

<section class="welcome">
  <h2 class="section-title">Welcome to My Website</h2>
  <p>Aliquam molestie, mi et imperdiet euismod, dui purus auctor tellus, et interdum lacus lectus et ante. Sed accumsan sollicitudin sapien, sit amet adipiscing turpis gravida ac. In congue, neque ac lobortis volutpat, libero mauris varius mi, vitae suscipit ipsum ligula vitae risus. Duis aliquam nibh a dui iaculis viverra id a velit. Vivamus egestas risus in magna varius commodo. Sed semper viverra egestas. Etiam pretium porttitor lectus, vel ornare neque porta volutpat.</p>
  <span class="btn">Read More</span>
</section>

<section class="range">
  <div class="wrap">
    <h2 class="section-title">Art Work Range</h2>
    <p class="section-lead">Aliquam molestie, mi et imperdiet euismod, dui purus auctor tellus, et interdum lacus lectus et ante.</p>
    <div class="art-grid">
      <div><div class="art-frame"><div class="art-fill" role="img" aria-label="Animation artwork" style="background:linear-gradient(135deg,#f4f4f4,#c9d3c0 60%,#8fa37a)"></div></div><div class="art-label">Animation</div></div>
      <div><div class="art-frame"><div class="art-fill" role="img" aria-label="Architecture sketch" style="background:linear-gradient(135deg,#f7f7f7,#d8d8d8)"></div></div><div class="art-label">Architecture</div></div>
      <div><div class="art-frame"><div class="art-fill" role="img" aria-label="Calligraphy alphabet" style="background:linear-gradient(135deg,#ffffff,#cfe6ee)"></div></div><div class="art-label">Calligraphy</div></div>
      <div><div class="art-frame"><div class="art-fill" role="img" aria-label="Religious artwork" style="background:linear-gradient(135deg,#f2ebe6,#c9a8a1)"></div></div><div class="art-label">Christian or Religious</div></div>
      <div><div class="art-frame"><div class="art-fill" role="img" aria-label="Artistic design collage" style="background:linear-gradient(90deg,#d9a58a,#efe3d6 50%,#a7573e)"></div></div><div class="art-label">Artistic Design</div></div>
      <div><div class="art-frame"><div class="art-fill" role="img" aria-label="Painting of a tree at sunset" style="background:linear-gradient(160deg,#3d5bb0,#c23f52 55%,#f1a640)"></div></div><div class="art-label">Painting</div></div>
      <div><div class="art-frame"><div class="art-fill" role="img" aria-label="Landscape photograph" style="background:linear-gradient(180deg,#e0a55b,#a46634 60%,#4d3420)"></div></div><div class="art-label">Photography</div></div>
      <div><div class="art-frame"><div class="art-fill" role="img" aria-label="Stone relief sculpture" style="background:linear-gradient(135deg,#7b7b7b,#3c3c3c)"></div></div><div class="art-label">Sculpture</div></div>
    </div>
    <span class="btn">View All Range</span>
  </div>
</section>

<section class="sale">
  <div class="wrap">
    <div class="sale-head">
      <h2>Art Works and Artifacts on Sale</h2>
      <svg width="36" height="18" viewBox="0 0 36 18"><path d="M10 2L3 9l7 7" fill="none" stroke="#333" stroke-width="3"/><path d="M26 2l7 7-7 7" fill="none" stroke="#f7780f" stroke-width="3"/></svg>
    </div>
    <div class="cards">
      <div class="card"><div class="card-img" role="img" aria-label="Colourful portrait painting" style="background:linear-gradient(135deg,#c77f5a,#8a6d8f 50%,#d9b48a)"></div><h3>Product Name</h3><p>Duis aliquam nibh a dui iaculis viverra</p><div class="price">$00.00</div><span class="cart"><svg width="16" height="14" viewBox="0 0 16 14"><path d="M0 1h3l2 7h8l2-5H4" fill="none" stroke="#fff" stroke-width="2"/><circle cx="6" cy="12" r="1.5" fill="#fff"/><circle cx="12" cy="12" r="1.5" fill="#fff"/></svg></span></div>
      <div class="card"><div class="card-img" role="img" aria-label="White plaster sculpture" style="background:linear-gradient(135deg,#f2f2f2,#bfbfbf)"></div><h3>Product Name</h3><p>Duis aliquam nibh a dui iaculis viverra</p><div class="price">$00.00</div><span class="cart"><svg width="16" height="14" viewBox="0 0 16 14"><path d="M0 1h3l2 7h8l2-5H4" fill="none" stroke="#fff" stroke-width="2"/><circle cx="6" cy="12" r="1.5" fill="#fff"/><circle cx="12" cy="12" r="1.5" fill="#fff"/></svg></span></div>
      <div class="card"><div class="card-img" role="img" aria-label="Photograph of a pier at dusk" style="background:linear-gradient(180deg,#9aa3ad,#d3b8a4 50%,#4f4a48)"></div><h3>Product Name</h3><p>Duis aliquam nibh a dui iaculis viverra</p><div class="price">$00.00</div><span class="cart"><svg width="16" height="14" viewBox="0 0 16 14"><path d="M0 1h3l2 7h8l2-5H4" fill="none" stroke="#fff" stroke-width="2"/><circle cx="6" cy="12" r="1.5" fill="#fff"/><circle cx="12" cy="12" r="1.5" fill="#fff"/></svg></span></div>
      <div class="card"><div class="card-img" role="img" aria-label="Calligraphy lettering print" style="background:linear-gradient(135deg,#dff0f5,#bcdbe6)"></div><h3>Product Name</h3><p>Duis aliquam nibh a dui iaculis viverra</p><div class="price">$00.00</div><span class="cart"><svg width="16" height="14" viewBox="0 0 16 14"><path d="M0 1h3l2 7h8l2-5H4" fill="none" stroke="#fff" stroke-width="2"/><circle cx="6" cy="12" r="1.5" fill="#fff"/><circle cx="12" cy="12" r="1.5" fill="#fff"/></svg></span></div>
    </div>
  </div>
</section>

<section class="split">
  <div class="news">
    <h2>News &amp; Events</h2>
    <div class="news-item">
      <div class="news-thumb" role="img" aria-label="Gallery exhibition room" style="background:linear-gradient(135deg,#b89a74,#6d4f3a)"></div>
      <div class="news-body"><div class="news-date">AUG 25, 2016</div><h3>Duis aliquam nibh a dui iaculis viverra</h3><p>Duis aliquam nibh a dui iaculis viverra id a velit. Vivamus egestas risus in magna varius commodo..</p></div>
    </div>
    <div class="news-item">
      <div class="news-thumb" role="img" aria-label="Visitors viewing paintings" style="background:linear-gradient(135deg,#4f8a6a,#a3744a)"></div>
      <div class="news-body"><div class="news-date">AUG 25, 2016</div><h3>Duis aliquam nibh a dui iaculis viverra</h3><p>Duis aliquam nibh a dui iaculis viverra id a velit. Vivamus egestas risus in magna varius commodo..</p></div>
    </div>
  </div>
  <div class="reviews">
    <h2>Reviews</h2>
    <div class="review">
      <div class="stars"><svg width="80" height="12" viewBox="0 0 80 12"><g fill="#ffd54a"><path id="s" d="M6 0l1.8 4 4.2.4-3.2 2.8 1 4.2L6 9.2 2.2 11.4l1-4.2L0 4.4 4.2 4z"/><use href="#s" x="16"/><use href="#s" x="32"/><use href="#s" x="48"/><use href="#s" x="64"/></g></svg></div>
      <h3>High End Creativity</h3>
      <p>Duis aliquam nibh a dui iaculis viverra id a velit. Vivamus egestas risus in magna varius commodo egestas risus in magna ..</p>
      <div class="by">-Name Heading</div>
    </div>
    <div class="review">
      <div class="stars"><svg width="80" height="12" viewBox="0 0 80 12"><g fill="#ffd54a"><use href="#s"/><use href="#s" x="16"/><use href="#s" x="32"/><use href="#s" x="48"/><use href="#s" x="64"/></g></svg></div>
      <h3>High End Creativity</h3>
      <p>Duis aliquam nibh a dui iaculis viverra id a velit. Vivamus egestas risus in magna varius commodo egestas risus in magna ..</p>
      <div class="by">-Name Heading</div>
    </div>
  </div>
</section>

<section class="signup">
  <h2 class="section-title">Join E-Mail Listing</h2>
  <p class="section-lead">Aliquam molestie, mi et imperdiet euismod, dui purus auctor tellus, et interdum lacus lectus et ante.</p>
  <div class="field first">Enter Name</div>
  <div class="field">Enter Email Address</div>
  <span class="btn">Subscribe</span>
</section>

<footer class="footer">
  <div class="fcol" style="left:76px"><h4>Site Map</h4><ul><li>Home</li><li>About Artist</li><li>Gallery</li><li>Sale</li><li>Blog</li><li>Reviews</li><li>News Event</li><li>Contact</li></ul></div>
  <div class="fcol" style="left:318px"><h4>Categories</h4><ul><li>Animation</li><li>Architecture</li><li>Assemblage</li><li>Calligraphy</li><li>Computer</li><li>Christian Or Religious</li><li>Conceptual</li><li>Artistic Design</li></ul></div>
  <div class="fcol cont" style="left:508px"><ul><li>Drawing</li><li>Folk</li><li>Graffiti</li><li>Graphic</li><li>Illuminated Manuscript</li><li>Illustration</li><li>Mosaic</li><li>Painting</li></ul></div>
  <div class="fcol cont" style="left:692px"><ul><li>Performance</li><li>Photography</li><li>Sculpture</li></ul></div>
  <div class="fcol contact" style="left:884px"><h4>Contact Info</h4>
    <div class="name">Quenmarsh Art</div>
    <div class="addr">412 Alder Lane,<br>Brookfield, NY 10231</div>
    <div class="row"><svg width="12" height="12" viewBox="0 0 12 12"><path d="M2 0h3l1 3-2 1a7 7 0 0 0 4 4l1-2 3 1v3c0 1-1 2-2 2C5 12 0 7 0 2c0-1 1-2 2-2z" fill="#ccc"/></svg>1800-555-0148</div>
    <div class="row"><svg width="13" height="10" viewBox="0 0 13 10"><rect width="13" height="10" fill="#ccc"/><path d="M0 0l6.5 5L13 0" fill="none" stroke="#2b2b2b" stroke-width="1.4"/></svg>hello@quenmarshart.com</div>
  </div>
</footer>
<div class="bottom">
  Copyright © 2016. Company Name. All Right Reserved
  <div class="socials"><span></span><span></span><span></span><span></span><span></span></div>
</div>

</body>
</html>
```